New Signage Design Project

Real estate company looking for signage, PowerPoint and stationery branding. Signs will be placed in front of homes and other properties being sold

Name of company is Tern Haven, LLC

Requirements
Must have
• Name of company - Tern Haven, LLC

```html
<!DOCTYPE html>
<html lang="en">
<head>
<meta charset="utf-8">
<title>Tern Haven, LLC — For Sale Sign</title>
<link href="https://fonts.googleapis.com/css2?family=Montserrat:wght@300;700;800&family=Roboto:wght@300&family=Roboto+Condensed:wght@400&display=swap" rel="stylesheet">
<style>
  :root {
    --backdrop: #d8d8d8;
    --sign: #222b2c;
    --coral: #e2515e;
    --sage: #86a5a3;
    --white: #ffffff;
  }
  * { margin: 0; padding: 0; box-sizing: border-box; }
  html, body {
    width: 1200px;
    height: 1200px;
    overflow: hidden;
    background: var(--backdrop);
  }
  .sign {
    position: absolute;
    left: 220px;
    top: 30px;
    width: 760px;
    height: 1140px;
    background: var(--sign);
  }
  .headline {
    position: absolute;
    left: 72px;
    color: var(--coral);
    font-family: "Montserrat", sans-serif;
    line-height: 1;
  }
  .headline-for {
    top: 28px;
    font-size: 146px;
    font-weight: 300;
    letter-spacing: -2px;
  }
  .headline-sale {
    top: 162px;
    font-size: 146px;
    font-weight: 800;
    letter-spacing: -3px;
  }
  .headline-rule {
    position: absolute;
    left: 62px;
    top: 322px;
    width: 230px;
    height: 7px;
    border-radius: 4px;
    background: var(--sage);
  }
  .agent-name {
    position: absolute;
    left: 0;
    right: 0;
    top: 412px;
    text-align: center;
    color: var(--white);
    font-family: "Montserrat", sans-serif;
    font-weight: 700;
    font-size: 82px;
    line-height: 1;
    letter-spacing: -1.5px;
  }
  .agent-rule {
    position: absolute;
    left: 124px;
    top: 515px;
    width: 512px;
    height: 6px;
  }
  .contact-phone {
    position: absolute;
    left: 0;
    right: 0;
    top: 538px;
    display: flex;
    justify-content: center;
    align-items: center;
    gap: 18px;
    color: var(--white);
    font-family: "Roboto", sans-serif;
    font-weight: 300;
    font-size: 74px;
    line-height: 1;
  }
  .phone-icon { width: 56px; height: 56px; flex: none; }
  .contact-web {
    position: absolute;
    left: 0;
    right: 0;
    top: 624px;
    text-align: center;
    color: var(--white);
    font-family: "Roboto Condensed", sans-serif;
    font-weight: 400;
    font-size: 50px;
    line-height: 1;
  }
  .brand {
    position: absolute;
    left: 0;
    right: 0;
    top: 880px;
    display: flex;
    justify-content: center;
    align-items: center;
    gap: 20px;
  }
  .brand-mark {
    width: 44px;
    height: 44px;
    background: var(--sage);
  }
  .brand-name {
    color: var(--white);
    font-family: "Montserrat", sans-serif;
    font-weight: 700;
    font-size: 54px;
    line-height: 1;
  }
</style>
</head>
<body>
  <main class="sign">
    <div class="headline headline-for">FOR</div>
    <div class="headline headline-sale">SALE</div>
    <div class="headline-rule"></div>

    <h1 class="agent-name">MARCUS WELLE</h1>
    <svg class="agent-rule" viewBox="0 0 512 6" preserveAspectRatio="none" aria-hidden="true">
      <path d="M0 3 Q256 -1 512 3 Q256 7 0 3 Z" fill="var(--coral)"/>
    </svg>

    <div class="contact-phone">
      <svg class="phone-icon" viewBox="0 0 56 56" aria-hidden="true">
        <path d="M8 8 C2 10 0 18 6 28 C12 38 22 48 32 52 C38 54 44 52 46 48 C47 45 45 43 42 42 L36 41 C34 41 33 43 32 44 C26 41 20 34 17 28 C18 27 20 26 20 24 L18 12 C17 8 12 7 8 8 Z" fill="var(--coral)"/>
        <path d="M28 16 A10 10 0 0 1 38 26" stroke="var(--coral)" stroke-width="2.5" fill="none" stroke-linecap="round"/>
        <path d="M28 9 A17 17 0 0 1 45 26" stroke="var(--coral)" stroke-width="2.5" fill="none" stroke-linecap="round"/>
        <path d="M28 2 A24 24 0 0 1 52 26" stroke="var(--coral)" stroke-width="2.5" fill="none" stroke-linecap="round"/>
      </svg>
      <span class="phone-number">800-555-0142</span>
    </div>
    <div class="contact-web">www.ternhavenllc.com</div>

    <div class="brand">
      <span class="brand-mark" aria-hidden="true"></span>
      <span class="brand-name">Tern Haven, LLC</span>
    </div>
  </main>
</body>
</html>
```